Flyer/Broschürre für Ambulanter Betreuungsdienst
Zielgruppe
Ambulanter Betreuungsdienst,Dienstleistungen für Senioren und Menschen mit Beeinträchtigung
Nach Paragraph 43b 45a/b & 53b SGBXI
Unterstützung im Alltag:
-Begleitung zu Arztbesuchen,Therapien &Terminbegleitung aller Art,
-Hilfe beim Einkaufen & Besorgungen + Transport
-Unterstützung bei der Tagesstrukturierung & Organisation im Alltag
-Erinnerungsservice zb. Einahme von Medikamenten ggbf. Kontrolle
-Begleitung zu Sportveranstaltungen,Theater uvm.
für zuverlässige Sicherheit und Orientierung.
-Gemeinsames Spazieren gehen ( Bewegungsangebote)
- Lesen & Vorlesen
-Gemeinsames Kochen und geselschaft leisten beim essen.
-Unterstützung bei Terminplanungen,Hilfe bei der komunikation mit Medizinischen Personal.
Soziale Betreuung & Aktivierung:
-Geselschaft leisten,Gespräche führen ;
-Freizeitaktivitäten Planen & Durchführen
-Gemeinsames Lesen und Vorlesen
-Karten & Brettspiele spielen
-Malen & Basteln
-Briefe schreiben,Emails verfassen
-Gemeinsam alte interessen wecken und neue finden.
-Angehörige entlasten
-kommunikation & Informationsaustausch über Fortschritte und Bedürfnisse
-Betreuung & Aktivierung für Menschen mit Demenz
-Erinnerungspflege,Biografie Arbeit
-Individuelle Betreuung
-Kurz und Langzeit Betreuung
-Nachtpflege
-Bewegungsangebote
-Spiele spielen zb. Brett & Gemeinschsftsspiele
Dienstleistungen Haushaltsbereich
-Reinigung von Böden(Saugen & Wischen)
-Reinigung Küche und Bad
-Bett frisch Beziehen
-Fenster Reinigung (innen & außen)
-Haustiere versorgen (mit dem Hund spazieren gehen)
-Wäsche waschen
-Dekorieren
-uvm
Aufgabenstellung
Freundliches Design , vertrauenswürdiges Erscheinungsbild mit warmen Farben.
Firmenname ( Sonnwerk) logo sollte einen Sonnwerk darstellen.
Slogan Text:
Verlässlichkeit und Fürsorge mit Herz & Verstand.
Format soll handlich und nicht zu klein sein,damit Senioren es gut lesen bzw erkennen können.

```html
<!DOCTYPE html>
<html lang="de">
<head>
<meta charset="utf-8">
<title>Sonnwerk – Ambulanter Betreuungsdienst</title>
<link href="https://fonts.googleapis.com/css2?family=Nunito:wght@400;500;800;900&display=swap" rel="stylesheet">
<style>
  :root{
    --bg:#d5e5f6;
    --ink:#1b2140;
    --photo-care:#b9b3ad;
    --photo-care-dark:#4d5466;
    --photo-couple:#c49a6c;
    --photo-couple-dark:#4f8ba5;
    --blush:#f6dfe0;
    --sky:#a9c2e2;
    --orange:#f08c41;
  }
  *{margin:0;padding:0;box-sizing:border-box}
  html,body{width:1200px;height:848px;overflow:hidden;background:var(--bg)}
  body{font-family:"Nunito",sans-serif;color:var(--ink);position:relative}
  .canvas{position:relative;width:1200px;height:848px;background:var(--bg);overflow:hidden}
  .abs{position:absolute}
  .photo-band{left:0;top:0;width:808px;height:245px}
  .brand{right:28px;top:40px;font-size:40px;font-weight:500;letter-spacing:.3px;display:flex;align-items:center;gap:10px;white-space:nowrap}
  .brand-dot{width:14px;height:14px;border-radius:50%;background:var(--ink)}
  .slogan{left:848px;top:136px;width:345px;font-size:45px;font-weight:900;line-height:55.5px}
  .divider{left:848px;top:376px;width:324px;height:1.5px;background:var(--ink)}
  .tagline{left:848px;top:398px;font-size:19.5px;line-height:24.5px;font-weight:500;white-space:nowrap}
  h2{font-weight:900;font-size:33px;line-height:41px;letter-spacing:.2px}
  .services{left:41px;top:262px}
  .service-list{list-style:none;position:absolute;left:41px;top:357px;width:380px}
  .service-list li{position:relative;padding-left:33px;font-size:19px;line-height:24px;margin-bottom:12px;font-weight:500}
  .service-list li::before{content:"";position:absolute;left:0;top:7px;width:11px;height:11px;border-radius:50%;background:var(--ink)}
  .contact{left:445px;top:262px}
  .company{left:445px;top:316px;font-size:19px;line-height:24px;font-weight:500}
  .contact-row{left:445px;display:flex;align-items:center;font-size:19px;line-height:24px;font-weight:500}
  .contact-row svg{width:30px;height:34px;margin-right:30px;flex:none}
  .areas-title{left:445px;top:606px}
  .areas{left:445px;top:655px;font-size:19px;line-height:24px;font-weight:500}
  .illustration{left:760px;top:575px;width:440px;height:273px}
</style>
</head>
<body>
<div class="canvas">

  <svg class="abs photo-band" viewBox="0 0 808 245">
    <defs>
      <clipPath id="band-curve">
        <path d="M0 0H808V190Q560 255 404 242Q200 232 0 198Z"/>
      </clipPath>
      <linearGradient id="care-tone" x1="0" y1="0" x2="1" y2="1">
        <stop offset="0" stop-color="#eef0f2"/>
        <stop offset=".55" stop-color="var(--photo-care)"/>
        <stop offset="1" stop-color="var(--photo-care-dark)"/>
      </linearGradient>
      <linearGradient id="couple-tone" x1="0" y1="0" x2="1" y2="1">
        <stop offset="0" stop-color="#7e9a5a"/>
        <stop offset=".5" stop-color="var(--photo-couple)"/>
        <stop offset="1" stop-color="var(--photo-couple-dark)"/>
      </linearGradient>
    </defs>
    <g clip-path="url(#band-curve)">
      <rect role="img" aria-label="Foto: Betreuerin schiebt einen Rollstuhl mit älterem Mann" x="0" y="0" width="404" height="245" fill="url(#care-tone)"/>
      <rect role="img" aria-label="Foto: Seniorenpaar formt mit den Händen ein Herz" x="404" y="0" width="404" height="245" fill="url(#couple-tone)"/>
    </g>
  </svg>

  <div class="abs brand"><span class="brand-dot"></span>Sonnwerk</div>

  <h1 class="abs slogan">Verlässlichkeit und Fürsorge mit Herz und Verstand.</h1>
  <div class="abs divider"></div>
  <p class="abs tagline">Ambulanter Betreuungsdienst,<br>Dienstleistungen für Senioren und<br>Menschen mit Beeintächtigung</p>

  <h2 class="abs services">Dienstleistungen<br>im Haushalt</h2>
  <ul class="service-list">
    <li>Bodenreinigung<br>(Saugen &amp; Wischen)</li>
    <li>Reinigung Küche und Bad</li>
    <li>Bettenmachen (frisch Beziehen)</li>
    <li>Fensterreinigung (innen &amp; außen)</li>
    <li>Haustierversorgung<br>(z.B. Spazieren mit Hund)</li>
    <li>Wäsche waschen</li>
    <li>Dekorieren und vieles mehr</li>
  </ul>

  <h2 class="abs contact">Kontakt</h2>
  <p class="abs company">Sonnwerk<br>Ambulanter Betreuungsdienst</p>

  <div class="abs contact-row" style="top:380px">
    <svg viewBox="0 0 30 34" fill="none" stroke="var(--ink)" stroke-width="1.4" stroke-linecap="round" stroke-linejoin="round">
      <path d="M6 8c-3 2-3 6 0 11s8 10 12 10c2 0 3-1 4-3l-4-4-3 2c-3-1-6-5-7-8l2-3-4-5z"/>
      <path d="M17 6a8 8 0 0 1 8 8M17 2a12 12 0 0 1 12 12M17 10a4 4 0 0 1 4 4"/>
    </svg>0123 456789
  </div>
  <div class="abs contact-row" style="top:429px">
    <svg viewBox="0 0 30 34" fill="none" stroke="var(--ink)" stroke-width="1.4" stroke-linecap="round">
      <path d="M15 30C9 21 5 16 5 11a10 10 0 0 1 20 0c0 5-4 10-10 19z"/>
      <circle cx="15" cy="11" r="4"/><path d="M11 32h8"/>
    </svg>Musterstraße 1<br>01234 Musterhausen
  </div>
  <div class="abs contact-row" style="top:492px">
    <svg viewBox="0 0 30 34" fill="none" stroke="var(--ink)" stroke-width="1.4" stroke-linecap="round" stroke-linejoin="round">
      <path d="M20 23H3V8h22v8M3 8l11 8 11-8"/>
      <circle cx="23" cy="24" r="5"/><circle cx="23" cy="24" r="2"/>
    </svg>emailadress@muster.de
  </div>
  <div class="abs contact-row" style="top:537px">
    <svg viewBox="0 0 30 34" fill="none" stroke="var(--ink)" stroke-width="1.4">
      <circle cx="15" cy="17" r="11"/><ellipse cx="15" cy="17" rx="5" ry="11"/>
      <path d="M4 17h22M6 11h18M6 23h18M15 6v22"/>
    </svg>www.musterwebsite.de
  </div>

  <h2 class="abs areas-title">Versorgungsgebiete</h2>
  <p class="abs areas">Musterstadt mit allen Stadtteilen<br>Musterweg, Musterwald, Musterhof</p>

  <svg class="abs illustration" viewBox="0 0 440 273" role="img" aria-label="Illustration: Seniorenpaar hält sich an den Händen, mit Pflanzen">
    <defs>
      <linearGradient id="illu-tone" x1="0" y1="0" x2="1" y2="1">
        <stop offset="0" stop-color="var(--blush)"/>
        <stop offset=".55" stop-color="#e9d5dd"/>
        <stop offset="1" stop-color="#f3c7a6"/>
      </linearGradient>
    </defs>
    <ellipse cx="246" cy="200" rx="188" ry="185" fill="url(#illu-tone)"/>
  </svg>

</div>
</body>
</html>
```